Brave Ladies - Fitness Retreat

Tri Fold Brochure & Double sided A4 version options, see attached mockup.

Target Market: Women 18-50, Asian mainly .

Kovo Fitness Presents - Brave Ladies Fitness Retreats:

Something communicating the spirit of getting fit, being strong, eating healthy and strong sense of the feminine.

Industry/Entity Type

Fitness

```html
<!DOCTYPE html>
<html lang="en">
<head>
<meta charset="utf-8">
<title>Kovo Fitness – Retreat Terms and Conditions</title>
<link href="https://fonts.googleapis.com/css2?family=Source+Sans+3:wght@400;600;700;900&display=swap" rel="stylesheet">
<style>
  :root {
    --backdrop: #e6e4df;
    --sheet-red: #b5222c;
    --sheet-red-light: #c4484f;
    --sheet-red-deep: #921a22;
    --ink-light: #fbeaea;
    --ink-white: #ffffff;
    --site-grey: #e9e9ec;
  }
  html, body {
    margin: 0;
    padding: 0;
    width: 1200px;
    height: 803px;
    overflow: hidden;
    background: var(--backdrop);
    font-family: "Source Sans 3", "Myriad Pro", Arial, sans-serif;
  }
  .canvas {
    position: relative;
    width: 1200px;
    height: 803px;
  }
  .sheet {
    position: absolute;
    left: 331px;
    top: 21px;
    width: 537px;
    height: 760px;
    box-sizing: border-box;
    padding: 56px 48px 0 48px;
    background: radial-gradient(ellipse 90% 55% at 30% 5%, var(--sheet-red-light) 0%, var(--sheet-red) 55%, var(--sheet-red-deep) 100%);
    color: var(--ink-light);
    box-shadow: 0 2px 10px rgba(0,0,0,0.15);
  }
  .terms-title {
    margin: 0 0 6px 0;
    font-size: 11px;
    font-weight: 700;
    letter-spacing: 0.02em;
    color: var(--ink-white);
  }
  .terms-list {
    margin: 0;
    padding-left: 14px;
    font-size: 9.5px;
    line-height: 1.35;
  }
  .terms-list li {
    margin-bottom: 5px;
  }
  .terms-list strong {
    font-weight: 700;
    color: var(--ink-white);
  }
  .brand {
    position: absolute;
    left: 0;
    right: 0;
    top: 468px;
    display: flex;
    justify-content: center;
    align-items: center;
    gap: 10px;
  }
  .brand-mark {
    width: 20px;
    height: 20px;
    background: var(--ink-white);
  }
  .brand-name {
    font-size: 26px;
    font-weight: 700;
    color: var(--ink-white);
  }
  .contact {
    position: absolute;
    left: 0;
    right: 0;
    top: 560px;
    text-align: center;
    color: var(--ink-white);
  }
  .contact-heading {
    margin: 0 0 12px 0;
    font-size: 11px;
    font-weight: 700;
  }
  .contact-line {
    margin: 0;
    font-size: 10.5px;
    line-height: 1.3;
  }
  .website {
    margin: 14px 0 0 0;
    font-size: 19px;
    font-weight: 900;
    letter-spacing: 0.01em;
    color: var(--site-grey);
  }
</style>
</head>
<body>
<main class="canvas">
  <section class="sheet">
    <h2 class="terms-title">TERMS AND CONDITIONS</h2>
    <ul class="terms-list">
      <li>Travel Insurance is mandatory for all of our guests</li>
      <li>Please confirm any special dietary needs before booking. Please note that for reasons of safety we cannot take guests who have a fatal allergy to any food/food groups. We are unable to provide separate meals and are very aware that the closest hospital may be up to 2 hours away.</li>
      <li>All clients to complete a <strong>Fitness &amp; Health Assessment</strong> from Trainer and to be completed prior to booking.</li>
      <li>Installment Payment is possible</li>
      <li>To secure your retreat we require a non-refundable deposit of $500pp</li>
      <li>Final payment to be made 30 days prior to arrival date. Cancellation fees may apply</li>
      <li>All funds are non-refundable if a guest chooses to cancel within 30 days of retreat start date.</li>
      <li>Refunds/credits will not be given after journey commencement, even if services, activities or meals are unused or cancelled for any reason</li>
      <li>Personal expenses to be paid in cash at end of retreat (laundry, drinks etc)</li>
      <li>We operate rain, hail or shine!</li>
    </ul>

    <div class="brand">
      <span class="brand-mark"></span>
      <span class="brand-name">Kovo Fitness</span>
    </div>

    <div class="contact">
      <p class="contact-heading">Further Info:</p>
      <p class="contact-line">+62 811.4063.2958</p>
      <p class="contact-line">coach.kovofitness@mail.com</p>
      <p class="website">WWW.KOVO-FITNESS.COM</p>
    </div>
  </section>
</main>
</body>
</html>
```